Redesign of existing website for a corporate advisory business focussed on technology

We need a redesign of our website. We are a corporate advisory business based in Sydney. Our focus is on the technology and life-science sectors. We assist our clients with capital raisings, mergers and acquisitions and other corporate transactions.

Our business is called "Harbourline Capital Advisors"
Our current website is www.harbourlinecap.com.au

I'd like to see a complete re-design of the site. (I'm happy to keep any of the existing images - but equally happy to scrap them completely and "start again".)

My preference is that the logo remain as it is. However, I would be very open to a re-colouring of the logo if it works better with a new webiste design.

The content of the website will remain the same. I'd like one additional section - "News" - which will allow us to manually post news items and which will pull in news feeds from current and past clients.

In terms of positioning / look-and-feel:

Our clients fall into two categories. I'd like the website to appeal to both:

1. The first category is: Executives from established technology or life-science companies (private or public), who engage us to assist with strategy, capital raising, corporate transactions.

2. The second category is: Entrepreneurs looking for advice in accessing angel funding or venture capital. The site should appeal to young tech-savvy entrepreneurs who are looking to engage a firm to provide such assistance.

To accomodate both target groups, the overriding feel should be one of professionalism, stability, trust and expertise. However, while the site should look fairly "corporate", I'd like it to feel contemporary and have an element of creativity and flair, reflecting the fact that our clients are often early-stage, innovative, technology companies. (I know this might be a tricky balance...)

Target Market(s)

Potential clients. Typically executives at technology or life-science companies or (more typically) entrepreneurs building their own companies

Industry/Entity Type

Business

Requirements
Must have
• 1. All content on the existing website
2. An additional section called "News" that allows us to easily add news items or articles and ideally which accepts news feeds from a handful of past and present clients
3. An ability to easily update and edit content
Should not have
• The site should not have "gimmicks". (Definitely no devices like the moving arrow in the current site!)

It should be fairly conservative, while still feeling contemporary and fresh.

```html
<!DOCTYPE html>
<html lang="en">
<head>
<meta charset="utf-8">
<title>Harbourline Capital Advisors</title>
<link rel="stylesheet" href="https://fonts.googleapis.com/css2?family=Source+Sans+3:wght@300;400;600;700;800;900&family=Arimo:ital,wght@0,400;0,700;1,700&display=swap">
<style>
:root{
  --orange:#e8591a;
  --orange-light:#f47b3c;
  --ink:#222;
  --grey:#666;
  --body:#444;
  --hero-top:#f4f4f4;
  --hero-mid:#e2e2e2;
  --nav-top:#5a5a5a;
  --nav-bottom:#1e1e1e;
  --footer:#1f2830;
  --line:#e3e3e3;
}
*{margin:0;padding:0;box-sizing:border-box}
html,body{width:1200px;height:1075px;overflow:hidden;background:#fff}
body{position:relative;font-family:"Source Sans 3",sans-serif;color:var(--ink)}
.abs{position:absolute}

/* header */
.brand-mark{left:131px;top:10px;width:90px;height:90px;border-radius:50%;background:var(--orange)}
.brand-name{left:236px;top:32px;font-size:31px;font-weight:400;color:#333;letter-spacing:.2px}
.connect{left:759px;top:52px;font-size:21px;font-weight:600;color:#444;display:flex;align-items:center;gap:10px}
.social{top:55px;width:26px;height:26px;border-radius:4px}
.social.s1{left:960px;background:#5fc4e8}
.social.s2{left:1002px;background:#1b6fa8}
.social.s3{left:1039px;background:#3b5b9a}
.header-rule{left:0;top:140px;width:1200px;height:1px;background:var(--line)}

/* hero */
.hero{left:0;top:141px;width:1200px;height:384px;background:radial-gradient(ellipse 420px 260px at 520px 170px,#fff 0%,rgba(255,255,255,0) 100%),linear-gradient(180deg,var(--hero-top),var(--hero-mid))}
.nav{left:124px;top:121px;width:955px;height:48px;border-radius:13px;background:linear-gradient(180deg,var(--nav-top),var(--nav-bottom));display:flex}
.nav-item{position:absolute;top:0;height:48px;line-height:48px;color:#fff;font-size:14px;font-weight:700;text-align:center}
.nav-item.home{left:58px;top:-7px;width:95px;height:55px;line-height:62px;background:linear-gradient(180deg,var(--orange-light),var(--orange))}
.nav-sep{position:absolute;top:0;width:1px;height:48px;background:#111;box-shadow:1px 0 0 #666}

.hero-line1{left:130px;top:200px;font-size:37px;font-weight:300;color:var(--orange)}
.hero-line2{left:130px;top:238px;font-size:35.5px;font-weight:800;color:var(--ink);letter-spacing:.5px}
.hero-line3{left:130px;top:276px;font-size:35.5px;font-weight:800;color:var(--orange);letter-spacing:.5px}
.hero-copy{left:131px;top:341px;width:431px;font-family:Arimo,sans-serif;font-size:13.4px;line-height:18.8px;color:#555;text-align:justify}
.hero-copy b{font-style:italic;color:#444}
.btn{left:130px;top:465px;width:136px;height:36px;border-radius:18px;background:linear-gradient(180deg,#f7935b,var(--orange));color:#fff;font-size:16px;font-weight:600;text-align:center;line-height:36px;box-shadow:0 1px 2px rgba(0,0,0,.3)}
.chart{left:664px;top:196px;width:369px;height:265px;border-radius:22px;background:linear-gradient(180deg,#3a3a3a,#050505 45%,#000);border:3px solid #111}
.chart-reflection{left:670px;top:465px;width:357px;height:60px;border-radius:14px;background:linear-gradient(180deg,rgba(0,0,0,.12),rgba(0,0,0,0))}

/* features */
.feature{top:548px;width:320px}
.feature-dot{position:absolute;left:0;top:1px;width:44px;height:44px;border-radius:50%;background:var(--orange)}
.feature h3{position:absolute;left:58px;top:-1px;font-size:21px;font-weight:700;color:#666;white-space:nowrap}
.feature .tag{position:absolute;left:57px;top:26px;font-size:15px;font-weight:700;color:var(--orange);white-space:nowrap}
.feature p{position:absolute;left:6px;top:66px;width:300px;font-size:12.6px;font-weight:600;line-height:19px;color:#444}
.feature .more{position:absolute;left:6px;top:134px;font-size:13.5px;color:#444;display:flex;align-items:center;gap:8px}
.feature .more span{text-decoration:underline}
.col-divider{top:552px;width:1px;height:148px;background:linear-gradient(180deg,rgba(0,0,0,0),#e0e0e0 30%,#e0e0e0 70%,rgba(0,0,0,0))}

/* about */
.about-title{left:99px;top:753px;font-size:21px;font-weight:600;color:var(--orange)}
.about-title span{color:#222}
.team-photo{left:97px;top:806px;width:208px;height:150px;background:linear-gradient(180deg,#dfe6ef,#8ea3bd 60%,#2d3a4a)}
.team-shadow{left:90px;top:958px;width:222px;height:14px;background:radial-gradient(ellipse at center top,rgba(0,0,0,.25),rgba(0,0,0,0) 70%)}
.about-copy{left:321px;top:813px;width:433px;font-family:Arimo,sans-serif;font-size:12.4px;line-height:18.8px;color:#444;text-align:justify}
.about-copy b{color:#222}
.about-copy p+p{margin-top:18px}
.view-more{font-family:Arimo,sans-serif;font-size:12.6px;color:var(--orange)}
.about-more{left:671px;top:958px}

/* articles */
.articles{left:815px;top:760px;width:279px;height:218px;border-radius:8px;border:1px solid #ddd;background:linear-gradient(180deg,#fff,#ececec);box-shadow:0 4px 0 #d4d4d4}
.ribbon{left:809px;top:780px;width:238px;height:31px;border-radius:0 7px 7px 0;background:linear-gradient(180deg,var(--orange-light),var(--orange));color:#fff;font-size:20px;font-weight:700;line-height:31px;padding-left:26px}
.ribbon-fold{left:809px;top:772px;width:0;height:0;border-left:7px solid transparent;border-bottom:8px solid #a83d0d}
.article{left:831px;width:252px}
.avatar{position:absolute;left:0;top:0;width:44px;height:37px;background:#c9a68a;border:3px solid #e6e6e6;box-shadow:0 0 0 1px #ccc}
.article-title{position:absolute;left:53px;top:0;width:200px;font-family:Arimo,sans-serif;font-size:12.6px;font-weight:700;line-height:18.8px;color:#222}
.article-title span{font-weight:400}
.article-meta{position:absolute;left:53px;top:38px;font-family:Arimo,sans-serif;font-size:12.4px;color:#333;letter-spacing:.4px;white-space:nowrap}
.articles-more{left:992px;top:950px}

/* footer */
.footer{left:0;top:1028px;width:1200px;height:47px;background:linear-gradient(180deg,#2a3540,var(--footer));color:#d6d6d6;font-size:14.5px;text-align:center;line-height:47px}
</style>
</head>
<body>
<header>
  <div class="abs hero"></div>
  <div class="abs brand-mark"></div>
  <div class="abs brand-name">Harbourline Capital Advisors</div>
  <div class="abs connect">Connect with us
    <svg width="24" height="20" viewBox="0 0 24 20"><path d="M2 10h17M12 3l8 7-8 7" fill="none" stroke="#f0692a" stroke-width="3.5" stroke-linecap="round" stroke-linejoin="round"/></svg>
  </div>
  <div class="abs social s1"></div>
  <div class="abs social s2"></div>
  <div class="abs social s3"></div>
  <div class="abs header-rule"></div>
  <nav class="abs nav">
    <div class="nav-item home">HOME</div>
    <div class="nav-sep" style="left:153px"></div>
    <div class="nav-item" style="left:154px;width:158px">OUR SERVICES</div>
    <div class="nav-sep" style="left:312px"></div>
    <div class="nav-item" style="left:313px;width:123px">OUR TEAM</div>
    <div class="nav-sep" style="left:436px"></div>
    <div class="nav-item" style="left:437px;width:157px">OUR EXPERIENCE</div>
    <div class="nav-sep" style="left:594px"></div>
    <div class="nav-item" style="left:612px">CONTACT US</div>
  </nav>
</header>

<section class="hero-content">
  <div class="abs hero-line1">A corporate advisory firm</div>
  <div class="abs hero-line2">with a focus on life-science</div>
  <div class="abs hero-line3">and technology !!</div>
  <p class="abs hero-copy"><b>Lorem ipsum dolor sit amet, consectetuer adipiscing elit. Nam nibh. Nunc varius facilisis eros.</b> Sed erat. In in velit quis arcu ornare laoreet. Curabitur adipiscing luctus massa. Integer ut purus ac augue commodo commodo. Nunc nec mi eu justo tempor consectetuer. Etiam vitae nisl.</p>
  <div class="abs btn">READ MORE....</div>
  <div class="abs chart" role="img" aria-label="Chalkboard tablet with a rising orange growth line"></div>
  <div class="abs chart-reflection"></div>
</section>

<section class="features">
  <div class="abs feature" style="left:101px">
    <div class="feature-dot"></div>
    <h3>Our Team</h3><div class="tag">aeserunt mollitia animi</div>
    <p>We work with Australian life-science and technology companies providing independent corporate advice and disciplined transaction execution capabilities</p>
    <div class="more"><svg width="14" height="14" viewBox="0 0 14 14"><circle cx="7" cy="7" r="7" fill="#ddd"/><path d="M5.5 4l4 3-4 3z" fill="#555"/></svg><span>Read More</span></div>
  </div>
  <div class="abs col-divider" style="left:422px"></div>
  <div class="abs feature" style="left:453px">
    <div class="feature-dot"></div>
    <h3>Our Services</h3><div class="tag" style="left:61px">aeserunt mollitia animi</div>
    <p style="left:8px">We work with Australian life-science and technology companies providing independent corporate advice and disciplined transaction execution capabilities</p>
    <div class="more" style="left:8px"><svg width="14" height="14" viewBox="0 0 14 14"><circle cx="7" cy="7" r="7" fill="#ddd"/><path d="M5.5 4l4 3-4 3z" fill="#555"/></svg><span>Read More</span></div>
  </div>
  <div class="abs col-divider" style="left:781px"></div>
  <div class="abs feature" style="left:803px">
    <div class="feature-dot"></div>
    <h3>Our Experience</h3><div class="tag" style="left:58px">aeserunt mollitia animi</div>
    <p>We work with Australian life-science and technology companies providing independent corporate advice and disciplined transaction execution capabilities</p>
    <div class="more"><svg width="14" height="14" viewBox="0 0 14 14"><circle cx="7" cy="7" r="7" fill="#ddd"/><path d="M5.5 4l4 3-4 3z" fill="#555"/></svg><span>Read More</span></div>
  </div>
</section>

<section class="about">
  <h2 class="abs about-title">A corporate advisory firm with a focus on <span>life-science and technology</span></h2>
  <div class="abs team-photo" role="img" aria-label="Silhouettes of business people standing before a world map"></div>
  <div class="abs team-shadow"></div>
  <div class="abs about-copy">
    <p><b>Harbourline Capital Advisors is a specialist corporate advisory and investment firm with a focus on high growth companies in the Australian life-science</b> and technology sectors.Our team combines extensive investment banking and funds management experience with sector expertise and longstanding investor relationships.</p>
    <p>Our advisory work incorporates both equity capital markets as well as mergers and acquisitions Via our alliance</p>
  </div>
  <div class="abs view-more about-more">View more [+]</div>
</section>

<aside>
  <div class="abs articles"></div>
  <div class="abs ribbon-fold"></div>
  <div class="abs ribbon">Latest Articles</div>
  <div class="abs article" style="top:830px">
    <div class="avatar" role="img" aria-label="Author portrait"></div>
    <div class="article-title">Lorem Ipsum is simply dummy text of the <span>printing</span></div>
    <div class="article-meta">May 15 , 2012 // 4 Comments</div>
  </div>
  <div class="abs article" style="top:892px">
    <div class="avatar" role="img" aria-label="Author portrait"></div>
    <div class="article-title">Lorem Ipsum is simply dummy text of the <span>printing</span></div>
    <div class="article-meta">May 15 , 2012 // 4 Comments</div>
  </div>
  <div class="abs view-more articles-more">View more [+]</div>
</aside>

<footer class="abs footer">Copyright @ Harbourline Capital Advisors Pty Ltd 2011, AFS License No: 512907</footer>
</body>
</html>
```